Screendesign für neue Website
Zielgruppe
Bauherren und alle die mal zum Architekten müssen.
Aufgabenstellung
Bei diesem Auftrag handelt es sich um die Erstellung eines Screendesigns für eine Website eines Archtiktenbüros.
Es wird daher ein Layout im PSD-Format erwartet, eine Umsetzung dessen in HTML wird nicht gefordert.

```html
<!DOCTYPE html>
<html lang="de">
<head>
<meta charset="utf-8">
<title>Planungsbüro Ahorn – Startseite</title>
<link rel="stylesheet" href="https://fonts.googleapis.com/css2?family=PT+Sans&family=Lato:wght@400;700&display=swap">
<style>
  :root {
    --bg-top: #2b2526;
    --bg-main: #1c1718;
    --bg-deep: #120e0f;
    --nav-fill: #140f10;
    --frame: #bdbdbd;
    --text-light: #f4f2f2;
    --text-muted: #6a6a6a;
    --footer-bg: #ffffff;
    --logo-ink: #111111;
  }
  * { margin: 0; padding: 0; box-sizing: border-box; }
  html, body { width: 1200px; height: 977px; overflow: hidden; background: var(--footer-bg); }
  .page { position: relative; width: 1200px; height: 977px; overflow: hidden; }

  .stage {
    position: absolute; left: 0; top: 0; width: 1200px; height: 849px;
    background: linear-gradient(to bottom, var(--bg-top) 0, #231d1e 127px, var(--bg-main) 290px, var(--bg-deep) 849px);
    border-bottom: 1px solid #8a8a8a;
  }
  .stage-backdrop {
    position: absolute; left: 520px; top: 290px; width: 620px; height: 559px;
    background: radial-gradient(ellipse at 55% 45%, rgba(70,62,63,0.55) 0, rgba(40,34,35,0.3) 45%, rgba(0,0,0,0) 75%);
  }

  .photo-strip {
    position: absolute; left: 51px; top: 127px; width: 1087px; height: 161px;
    display: flex; border: 1px solid #5a5556;
  }
  .photo-strip .photo { flex: 1; height: 100%; border-right: 1px solid #4a4445; }
  .photo-strip .photo:last-child { border-right: none; }
  .photo--facade { background: linear-gradient(135deg, #4a3a30, #a2643a 55%, #d9d2c8); }
  .photo--chair { background: linear-gradient(160deg, #c48a4a, #e0a866 50%, #8a5a2c); }
  .photo--railing { background: linear-gradient(150deg, #9c9a96, #e9e9e7 55%, #c4c4c0); }
  .photo--building { background: linear-gradient(to bottom, #6f8fb5 0, #c9d3dc 45%, #f1f1ef 65%, #5c8a3a 100%); }
  .photo--pool { background: linear-gradient(to bottom, #7fb3c0 0, #3fa6c6 55%, #d8dcdc 100%); }
  .photo--stairs { background: linear-gradient(135deg, #c89a5a, #e8d6b0 45%, #6a6e74); }
  .strip-band {
    position: absolute; left: 51px; top: 210px; width: 1087px; height: 51px;
    background: rgba(255,255,255,0.22);
  }

  .main-nav {
    position: absolute; left: 828px; top: 127px; width: 156px; height: 722px;
    border: 2px solid var(--frame); border-bottom: none;
  }
  .main-nav .nav-fill {
    position: absolute; left: 0; top: 159px; right: 0; bottom: 0; background: var(--nav-fill);
  }
  .nav-list { list-style: none; position: absolute; left: 845px; top: 0; }
  .nav-list li {
    position: absolute; left: 0; white-space: nowrap;
    font-family: "Lato", sans-serif; font-weight: 700; font-size: 14px;
    letter-spacing: 1.6px; color: var(--text-light); text-transform: uppercase;
  }

  .claim { font-family: "PT Sans", sans-serif; color: var(--text-light);
    text-shadow: 0 0 6px rgba(255,255,255,0.55), 0 0 14px rgba(255,255,255,0.25); }
  .claim-line { position: absolute; white-space: nowrap; font-size: 33px; line-height: 1; }

  .footer-link {
    position: absolute; left: 1084px; top: 861px;
    font-family: "Lato", sans-serif; font-size: 15px; color: var(--text-muted);
  }
  .brand {
    position: absolute; left: 48px; top: 880px; display: flex; align-items: center; gap: 10px;
    font-family: "Lato", sans-serif; font-weight: 700; font-size: 18px; color: var(--logo-ink);
  }
  .brand-square { width: 44px; height: 44px; background: var(--logo-ink); }
</style>
</head>
<body>
<div class="page">
  <div class="stage">
    <div class="stage-backdrop" role="img" aria-label="Unscharfes Hintergrundfoto in dunklen Grautönen"></div>

    <div class="photo-strip">
      <div class="photo photo--facade" role="img" aria-label="Foto: Fassade mit Holzlamellen"></div>
      <div class="photo photo--chair" role="img" aria-label="Foto: Holzstuhl im Detail"></div>
      <div class="photo photo--railing" role="img" aria-label="Foto: Treppe mit Metallgeländer"></div>
      <div class="photo photo--facade" role="img" aria-label="Foto: Fassade mit Holzlamellen"></div>
      <div class="photo photo--building" role="img" aria-label="Foto: weißer Rundbau mit Rasen"></div>
      <div class="photo photo--pool" role="img" aria-label="Foto: Schwimmbecken mit Treppe"></div>
      <div class="photo photo--stairs" role="img" aria-label="Foto: Treppenhaus mit Holzdecke"></div>
    </div>
    <div class="strip-band"></div>

    <nav class="main-nav" aria-label="Hauptnavigation"><div class="nav-fill"></div></nav>
    <ul class="nav-list">
      <li style="top:96px">Startseite</li>
      <li style="top:326px">Unternehmen</li>
      <li style="top:402px">Projekte</li>
      <li style="top:479px">Information</li>
      <li style="top:555px">Aktuelles</li>
      <li style="top:632px">Leistungen</li>
      <li style="top:708px">Kontakt</li>
    </ul>

    <div class="claim">
      <h1 class="claim-line" style="left:47px; top:356px; font-weight:400; font-size:33px;">Architekten schaffen:</h1>
      <p class="claim-line" style="left:246px; top:438px;">Lebens-Raum</p>
      <p class="claim-line" style="left:382px; top:521px;">Lebens-Traum</p>
      <p class="claim-line" style="left:540px; top:615px;">Traum Haus</p>
    </div>
  </div>

  <a class="footer-link">Impressum |</a>

  <div class="brand">
    <span class="brand-square"></span>
    <span>Planungsbüro Ahorn</span>
  </div>
</div>
</body>
</html>
```